Book Cover for Willow Kindred Notes from the Meadow

We have written a book that brings together Notes from the Meadow from a variety of women's voices.
We developed a draft book cover that we like using Canva (attached below). We'd love a book cover that is similar to this image, but looks more professional.
Following are the themes we’d like to depict in the book cover, and in parentheses, how they are represented in the current cover:
1. Divinely feminine (overall cover)
2. Currents of enlightenment (the swirls of light carrying the butterfly)
3. Diversity (a myriad of colors)
4. The solo journey into the unknown (the single butterfly’s flight)
5. Buoyancy and joy (again, the dancing colors and floating butterfly)
6. Boldly feminine (the blue butterfly, set against brush strokes of light)
7. Homage to a dear friend (she loved blue butterflies, the cosmos - this butterfly has hints of the cosmos in her wings, and painting - this background has brush strokes of light).
Book Title, Subtitle, and Editor:
Willow Kindred
Notes from the Meadow
Edited by Mirela Tove
Thank you very much for considering this project!
People who are interested in Women and Spirituality

```html
<!DOCTYPE html>
<html lang="en">
<head>
<meta charset="UTF-8">
<title>Willow Kindred — Notes from the Meadow</title>
<link rel="stylesheet" href="https://fonts.googleapis.com/css2?family=Sacramento&family=Poiret+One&family=Montserrat:wght@500&display=swap">
<style>
  :root {
    --title-blue: #2b2f9c;
    --subtitle-gold: #b7842c;
    --credit-white: #ffffff;
    --sky-teal: #bfe3e6;
    --sky-peach: #f4d7a8;
    --sky-rose: #d9a0b3;
    --sky-violet: #8e7aa8;
    --cloud-dusk: #6f5f6e;
    --wing-blue: #3d8fd6;
    --wing-deep: #3a3f9e;
  }
  html, body {
    margin: 0;
    padding: 0;
    overflow: hidden;
    background: #ffffff;
  }
  .cover {
    position: relative;
    width: 788px;
    height: 1200px;
    overflow: hidden;
  }
  .cover__sky {
    position: absolute;
    inset: 0;
    background:
      radial-gradient(ellipse 55% 35% at 55% 30%, rgba(255,255,255,0.85), rgba(255,255,255,0) 70%),
      radial-gradient(ellipse 40% 30% at 10% 40%, rgba(120,200,230,0.7), rgba(120,200,230,0) 70%),
      radial-gradient(ellipse 45% 25% at 85% 55%, rgba(240,160,110,0.6), rgba(240,160,110,0) 70%),
      radial-gradient(ellipse 50% 30% at 80% 75%, rgba(190,110,170,0.55), rgba(190,110,170,0) 70%),
      linear-gradient(180deg, #9aa0ad 0%, var(--sky-teal) 22%, var(--sky-peach) 45%, var(--sky-rose) 65%, var(--sky-violet) 80%, var(--cloud-dusk) 100%);
  }
  .cover__butterfly {
    position: absolute;
    left: 204px;
    top: 560px;
    width: 472px;
    height: 484px;
  }
  .cover__title {
    position: absolute;
    left: 0;
    top: 95px;
    width: 100%;
    margin: 0;
    font-family: "Sacramento", cursive;
    font-weight: 400;
    font-size: 185px;
    line-height: 172px;
    color: var(--title-blue);
    text-align: center;
  }
  .cover__title span { display: block; }
  .cover__title .line-two { padding-left: 20px; }
  .cover__subtitle {
    position: absolute;
    left: 0;
    top: 474px;
    width: 100%;
    margin: 0;
    font-family: "Poiret One", sans-serif;
    font-weight: 400;
    font-size: 46px;
    letter-spacing: 0;
    text-transform: uppercase;
    color: var(--subtitle-gold);
    text-align: center;
  }
  .cover__credit {
    position: absolute;
    left: 108px;
    top: 1090px;
    margin: 0;
    display: flex;
    align-items: baseline;
    gap: 22px;
    color: var(--credit-white);
  }
  .cover__credit-label {
    font-family: "Montserrat", sans-serif;
    font-weight: 500;
    font-size: 30px;
  }
  .cover__credit-name {
    font-family: "Sacramento", cursive;
    font-size: 84px;
    line-height: 1;
  }
</style>
</head>
<body>
  <main class="cover">
    <div class="cover__sky" role="img" aria-label="Painted sky with swirling rainbow brush strokes of light above soft dusky clouds"></div>

    <svg class="cover__butterfly" viewBox="0 0 472 484" role="img" aria-label="Illustration of a single blue butterfly with cosmic-speckled wings in flight">
      <defs>
        <radialGradient id="wing-tone" cx="50%" cy="50%" r="55%">
          <stop offset="0%" stop-color="var(--wing-blue)" stop-opacity="0.75"/>
          <stop offset="70%" stop-color="var(--wing-deep)" stop-opacity="0.45"/>
          <stop offset="100%" stop-color="var(--wing-deep)" stop-opacity="0"/>
        </radialGradient>
      </defs>
      <ellipse cx="236" cy="242" rx="236" ry="242" fill="url(#wing-tone)"/>
    </svg>

    <h1 class="cover__title">
      <span class="line-one">Willow</span>
      <span class="line-two">Kindred</span>
    </h1>

    <p class="cover__subtitle">Notes from the Meadow</p>

    <p class="cover__credit">
      <span class="cover__credit-label">Edited by</span>
      <span class="cover__credit-name">Mirela Tove</span>
    </p>
  </main>
</body>
</html>
```